RevelHubQZ Business Cards

Front
Has logo with a design. Website address (www.revelhubqz.example)
Has slogan (discover nightlife)
Has phone number (5129873304)
Should be bold and stands out.

Back
Has details about what we offer.

Events
Search upcoming events
Submit events
Party Image Gallery
View and download HQ party images
Sign up as a contributing event photographer and get paid!
Tickets
Sell your event tickets online for free!
Direct pay
No ticket fee

Target Market(s)

These cards will be handed out in clubs and events to patrons.

Industry/Entity Type

Business

Contact Information for Business Card

Should match or mirror our website in some sort of way. Visit the website to get ideas.

Requirements
Must have
• Must be designed for a 3x3 inch card.

```html
<!DOCTYPE html>
<html lang="en">
<head>
<meta charset="utf-8">
<title>RevelHubQZ Business Cards</title>
<link href="https://fonts.googleapis.com/css2?family=Montserrat:wght@400;500&display=swap" rel="stylesheet">
<style>
  :root {
    --stage: #e6e7e8;
    --brand-blue: #2ba6da;
    --brand-pink: #e4439a;
    --white: #ffffff;
    --tint-front: #e9f1f8;
    --tint-back: rgba(255, 255, 255, 0.14);
    --card-shadow: rgba(0, 0, 0, 0.35);
  }
  * { margin: 0; padding: 0; box-sizing: border-box; }
  html, body {
    width: 1200px; height: 927px; overflow: hidden;
    background: var(--stage);
    font-family: "Montserrat", sans-serif;
  }
  .stage { position: relative; width: 1200px; height: 927px; }
  .card {
    position: absolute; top: 221px; width: 485px; height: 485px;
    box-shadow: 7px 8px 10px var(--card-shadow);
    overflow: hidden;
  }
  .card--front { left: 96px; background: var(--white); }
  .card--back { left: 619px; background: var(--brand-blue); }

  .backdrop { position: absolute; left: 0; top: 0; width: 485px; height: 485px; }

  .wordmark {
    position: absolute; top: 26px; left: 0; width: 100%;
    text-align: center;
  }
  .wordmark__row { display: inline-flex; align-items: center; gap: 10px; }
  .wordmark__dot { width: 30px; height: 30px; border-radius: 50%; background: var(--brand-blue); }
  .wordmark__name { font-size: 38px; font-weight: 500; color: var(--brand-blue); letter-spacing: -0.5px; line-height: 44px; }
  .wordmark__slogan {
    display: block; margin-top: 0;
    font-size: 13px; letter-spacing: 5px; color: var(--brand-pink);
  }
  .card--back .wordmark { top: 30px; }
  .card--back .wordmark__dot { width: 22px; height: 22px; background: var(--white); }
  .card--back .wordmark__name { font-size: 28px; line-height: 34px; color: var(--white); }
  .card--back .wordmark__slogan { font-size: 10px; letter-spacing: 4.5px; color: var(--white); }

  .contact { position: absolute; left: 25px; top: 378px; color: var(--white); }
  .contact__name { font-size: 21px; font-weight: 500; letter-spacing: 1px; line-height: 26px; }
  .contact__role { font-size: 16px; letter-spacing: 0.5px; line-height: 22px; }
  .contact__line { font-size: 14px; letter-spacing: 0.5px; line-height: 18px; }
  .contact__line:first-of-type { margin-top: 6px; }
  .contact__label { font-weight: 500; }

  .offer-list {
    position: absolute; top: 141px; left: 0; width: 100%;
    list-style: none; text-align: center;
    color: var(--white); font-size: 14.5px; line-height: 19.8px; letter-spacing: 0.2px;
  }
</style>
</head>
<body>
<main class="stage">
  <section class="card card--front" aria-label="Card front">
    <svg class="backdrop" viewBox="0 0 485 485" aria-hidden="true">
      <circle cx="242" cy="200" r="125" fill="var(--tint-front)"/>
      <path d="M0,389 Q220,205 485,485 L465,485 Q215,228 0,396 Z" fill="var(--brand-pink)"/>
      <path d="M0,396 Q215,228 465,485 L0,485 Z" fill="var(--brand-blue)"/>
    </svg>
    <div class="wordmark">
      <div class="wordmark__row">
        <span class="wordmark__dot"></span>
        <span class="wordmark__name">RevelHubQZ</span>
      </div>
      <span class="wordmark__slogan">discover nightlife</span>
    </div>
    <div class="contact">
      <p class="contact__name">MARLO BENNETT</p>
      <p class="contact__role">Director</p>
      <p class="contact__line"><span class="contact__label">P:</span> 5129873304</p>
      <p class="contact__line"><span class="contact__label">W:</span> www.revelhubqz.example</p>
    </div>
  </section>

  <section class="card card--back" aria-label="Card back">
    <svg class="backdrop" viewBox="0 0 485 485" aria-hidden="true">
      <circle cx="242" cy="250" r="175" fill="var(--tint-back)"/>
    </svg>
    <div class="wordmark">
      <div class="wordmark__row">
        <span class="wordmark__dot"></span>
        <span class="wordmark__name">RevelHubQZ</span>
      </div>
      <span class="wordmark__slogan">discover nightlife</span>
    </div>
    <ul class="offer-list">
      <li>Events</li>
      <li>Search upcoming events</li>
      <li>Submit events</li>
      <li>Party Image Gallery</li>
      <li>View and download HQ party images</li>
      <li>Sign up as a contributing event photographer and get paid!</li>
      <li>Tickets</li>
      <li>Sell your event tickets online for free!</li>
      <li>Direct pay</li>
      <li>No ticket fee</li>
    </ul>
  </section>
</main>
</body>
</html>
```